Lindenhof Wissensportal - Redesign
Die Seite http://www.lindenhof-wissensportal.de soll einem kompletten neu designed werden. Der Inhalt soll so übernommen werden. Auf der Startseite soll ein Blog inegriert werden. Typische Features wie Zeitachsenarchiv, Tagclouds, letzte Kommentare und Social Media Links sollen intelligent integriert werden. Alle Menüpunkte sollen als Themenvorschläge auf der Wesite mit entsprechenden Bildern integriert werden.
Beispiel: Menüpunkt Top Emittenten. Auf der Wesite wird dann beispielsweise ein kleiner Kasten mit Headline "Wer sind die Besten?" inetgriert. Im Kasten ist ein ansprechends Bild und ein kurzer Text: "Die bseten Emittenten finden Sie hier!"
Ein intelligentes Cockpit soll den User auf jeder Seite begleiten. Hier wird der Newsletter angeboten und die Social Media Links verpackt. Darüber hinaus eine E-Mail zur Kontaktaufnahme.
Als Leitfarben sehen wir folgende Kombinationsmöglichkeiten:
a. Grau - Orange
b. Grau - Froschgrün
c. Graubraun - Orange
Bitte berücksichtigen Sie, dass unsere Besucher zwischen 40 und 70 Jahre alt sind.
Die späterr Programmierung soll in Wordpress stattfinden!
Bei weiteren Fragen wenden Sie sich gerne an mich.
Viel Erfolg!

```html
<!DOCTYPE html>
<html lang="de">
<head>
<meta charset="utf-8">
<title>Lindenhof Wissensportal</title>
<link href="https://fonts.googleapis.com/css2?family=Arimo:wght@400;700&display=swap" rel="stylesheet">
<style>
:root{
  --green:#3aa62a;
  --green-light:#5cc04a;
  --dark:#2b2b2b;
  --grey-bg:#f1f1f1;
  --text:#1a1a1a;
  --muted:#8c8c8c;
}
*{box-sizing:border-box;margin:0;padding:0}
html,body{width:800px;height:1200px;overflow:hidden;background:#fff}
body{font-family:"Arimo",Arial,sans-serif;color:var(--text);position:relative}
.page{position:absolute;left:14px;top:12px;width:773px;height:1104px;border:1px solid var(--green-light);border-top:none}
.abs{position:absolute}
.nav{left:0;top:0;width:773px;height:26px;display:flex;background:linear-gradient(#4a4a4a,#262626)}
.nav a{flex:1;color:#fff;font-size:10px;text-decoration:none;display:flex;align-items:center;justify-content:center;border-right:1px solid #666}
.nav a.active{background:var(--green)}
.crumb{left:0;top:26px;width:773px;height:12px;background:var(--green);color:#fff;font-size:7px;padding:2px 0 0 14px}
.hero-photo{left:1px;top:38px;width:256px;height:176px;background:radial-gradient(circle at 45% 50%,#e0a27c,#c97a52 45%,#f3f0ec 75%)}
.brand{left:286px;top:70px;font-size:28px;font-weight:700;color:var(--green)}
.slogan{left:470px;top:108px;width:230px;text-align:right;font-size:17px;color:#222}
.intro{left:465px;top:157px;width:308px;height:52px;border:1px solid var(--green-light);border-right:none;background:#fff;padding:6px 9px}
.intro h2{font-size:11px;font-weight:700;margin-bottom:4px}
.intro p{font-size:7.5px;line-height:11px}
.band{left:0;top:216px;width:773px;height:12px;background:#e2e2e2}
.teaser-img{width:76px;height:48px;border:1px solid #ccc}
.teaser h3{font-size:11.5px;color:var(--green);font-weight:700;margin-bottom:5px}
.teaser p{font-size:7.5px;line-height:10.5px;color:var(--muted)}
.cockpit{left:568px;width:205px;background:var(--grey-bg)}
.cockpit .label{font-size:11px;color:#111}
.mail-input{position:absolute;left:16px;top:30px;width:128px;height:16px;border:1px solid #aaa;background:#fff;font-size:8px;color:#888;padding:3px 6px}
.soc{width:20px;height:20px;border-radius:3px;background:var(--green)}
.section-head{height:24px;background:var(--grey-bg);border-bottom:1px solid var(--green-light);font-size:11px;padding:6px 0 0 12px}
.post{left:20px;width:462px}
.post h1{font-size:16px;color:var(--green);font-weight:700}
.post h2{font-size:13px;color:var(--green);font-weight:400;margin-bottom:18px}
.post p{font-size:9.6px;line-height:13.6px}
.post p+p{margin-top:13.6px}
.eggs{left:358px;top:444px;width:196px;height:86px;background:radial-gradient(ellipse at 50% 55%,#e2b530,#b07d12 45%,#f4f1ea 72%)}
.meta{left:1px;width:563px;height:20px;background:var(--grey-bg);font-size:8px;color:var(--muted);display:flex;align-items:center;padding-left:20px;gap:4px}
.like{border:1px solid #b7bfd4;background:#eef0f6;color:#3b4f8a;padding:1px 4px;margin-left:14px;font-size:8px}
.count{border:1px solid #bbb;background:#fff;padding:1px 5px;color:#333}
.side{left:568px;width:205px;background:var(--grey-bg)}
.archive li{list-style:none;font-size:9.6px;color:var(--muted);line-height:16px}
.comment{margin-bottom:17px}
.comment h4{font-size:9px;color:var(--muted);font-weight:700}
.comment p{font-size:9px;line-height:14.4px;color:var(--muted)}
.tag{position:absolute;font-weight:700;white-space:nowrap;letter-spacing:.6px}
</style>
</head>
<body>
<div class="page">
  <nav class="nav abs">
    <a class="active">Start</a><a>Warum Fonds?</a><a>Sektoren</a><a>Top Emittenten</a><a>Ratings</a><a>Kaufen ohne Agio</a><a>Newsletter</a>
  </nav>
  <div class="crumb abs">&gt; Startseite</div>

  <div class="hero-photo abs" role="img" aria-label="Porträtfoto eines lächelnden Beraters mit Brille"></div>
  <div class="brand abs">Lindenhof Wissensportal</div>
  <div class="slogan abs">...suchen lohnt sich.</div>
  <div class="intro abs">
    <h2>Lorem ipsum</h2>
    <p>Lorem ipsum dolor sit amet, consetetur sadipscing elitr, sed diam nonumy eir mod tempor invidunt ut dolor sit amet, consetetur sadipscing elitr....</p>
  </div>
  <div class="band abs"></div>

  <div class="teaser-img abs" style="left:12px;top:249px;background:linear-gradient(#e8e8e8,#9a9a9a)" role="img" aria-label="Grünes Fragezeichen auf Steinhaufen"></div>
  <div class="teaser abs" style="left:96px;top:253px;width:100px"><h3>Warum Fonds?</h3><p>Aus welchem Grund investiere ich mein Geld in geschlossene Fonds?</p></div>

  <div class="teaser-img abs" style="left:208px;top:249px;background:linear-gradient(#fafafa,#d0d0d0)" role="img" aria-label="Aufgefächerte Spielkarten"></div>
  <div class="teaser abs" style="left:291px;top:253px;width:80px"><h3>Sektoren</h3><p>Vier Sektoren in meinem Fokus!</p></div>

  <div class="teaser-img abs" style="left:380px;top:249px;background:linear-gradient(#fff,#7ccd5a 60%,#3c9a2a)" role="img" aria-label="Grüne Krone"></div>
  <div class="teaser abs" style="left:462px;top:253px;width:100px"><h3>Top Emittenten</h3><p>Geben Sie sich nur mit den Besten zufrieden!</p></div>

  <div class="teaser-img abs" style="left:14px;top:325px;background:linear-gradient(90deg,#f4f4f4,#8fd07a)" role="img" aria-label="Steigendes Balkendiagramm mit Kurve"></div>
  <div class="teaser abs" style="left:98px;top:328px;width:100px"><h3>Ratings</h3><p>Ratingagenturen sind Meinungsmacher und werden meist von...</p></div>

  <div class="teaser-img abs" style="left:208px;top:325px;background:linear-gradient(#f8f8f8,#5cb844)" role="img" aria-label="Grüner Schriftzug Null Prozent"></div>
  <div class="teaser abs" style="left:292px;top:328px;width:110px"><h3>Kaufen ohne Agio</h3><p>Im Einkauf liegt der Gewinn und heute kauft man ge-schlossene Fonds im...</p></div>

  <div class="cockpit abs" style="top:230px;height:61px">
    <div class="label abs" style="left:16px;top:12px">Newsletter bestellen</div>
    <div class="mail-input">Emailadresse</div>
    <svg class="abs" style="left:147px;top:33px" width="7" height="10"><path d="M0 0L7 5L0 10Z" fill="var(--green)"/></svg>
    <svg class="abs" style="left:160px;top:8px" width="36" height="34" viewBox="0 0 36 34"><path d="M2 12L22 2L34 22L14 32Z" fill="#e9e9e9" stroke="#666" stroke-width="1.5"/><path d="M2 12L20 18L22 2M20 18L14 32" fill="none" stroke="#666" stroke-width="1.2"/></svg>
  </div>
  <div class="cockpit abs" style="top:294px;height:48px">
    <div class="label abs" style="left:18px;top:18px">Schreiben Sie uns eine Email</div>
    <svg class="abs" style="left:160px;top:8px" width="36" height="34" viewBox="0 0 36 34"><path d="M2 12L22 2L34 22L14 32Z" fill="#e9e9e9" stroke="#666" stroke-width="1.5"/><path d="M2 12L20 18L22 2M20 18L14 32" fill="none" stroke="#666" stroke-width="1.2"/><circle cx="28" cy="7" r="5" fill="none" stroke="#666" stroke-width="1.4"/></svg>
  </div>
  <div class="cockpit abs" style="top:346px;height:40px">
    <div class="soc abs" style="left:19px;top:11px"></div>
    <div class="soc abs" style="left:50px;top:11px"></div>
    <div class="soc abs" style="left:81px;top:11px"></div>
  </div>

  <div class="section-head abs" style="left:1px;top:392px;width:563px">Blog</div>
  <div class="side abs" style="top:392px;height:712px"></div>
  <div class="section-head abs" style="left:568px;top:392px;width:205px">Archiv</div>
  <ul class="archive abs" style="left:582px;top:436px">
    <li>Januar 2011</li><li>Februar 2011</li><li>März 2011</li><li>April 2011</li><li>Mai 2011</li>
  </ul>
  <div class="section-head abs" style="left:568px;top:548px;width:205px">Letzte Kommentare</div>
  <div class="abs" style="left:582px;top:586px;width:168px">
    <div class="comment"><h4>Lorem ipsum</h4><p>dolor sit amet, consetetur sadipscing elitr, sed diam nonumy eirmodtempor invidunt ut labore et dolore magna aliquyam erat, sed diam voluptua...</p></div>
    <div class="comment"><h4>Lorem ipsum</h4><p>dolor sit amet, consetetur sadipscing elitr, sed diam nonumy eirmodtempor invidunt ut labore et dolore magna aliquyam erat, sed diam voluptua...</p></div>
    <div class="comment"><h4>Lorem ipsum</h4><p>dolor sit amet, consetetur sadipscing elitr, sed diam nonumy eirmodtempor invidunt ut labore et dolore magna aliquyam erat, sed diam voluptua...</p></div>
  </div>
  <div class="section-head abs" style="left:568px;top:868px;width:205px">Tag Cloud</div>
  <div class="abs" style="left:568px;top:894px;width:205px;height:210px">
    <span class="tag" style="left:50px;top:10px;font-size:14px;color:#111">Leistungsbilanz</span>
    <span class="tag" style="left:115px;top:28px;font-size:12px;color:#bbb">Schiffsfonds</span>
    <span class="tag" style="left:20px;top:43px;font-size:17px;color:#999">Investitionsquote</span>
    <span class="tag" style="left:9px;top:68px;font-size:10px;color:#bbb">Ausfallwagnis</span>
    <span class="tag" style="left:50px;top:86px;font-size:11px;color:#888">Agio</span>
    <span class="tag" style="left:86px;top:76px;font-size:24px;color:#111">Rendite</span>
    <span class="tag" style="left:21px;top:108px;font-size:15px;color:#bbb">Finanzierungsstruktur</span>
    <span class="tag" style="left:9px;top:130px;font-size:17px;color:#111">Flugzeugfonds</span>
    <span class="tag" style="left:110px;top:150px;font-size:10px;color:#888">Inflationsschutz</span>
    <span class="tag" style="left:18px;top:162px;font-size:12px;color:#777;font-weight:400">Umweltfonds</span>
    <span class="tag" style="left:96px;top:162px;font-size:25px;color:#bbb">Gewinn</span>
  </div>

  <div class="eggs abs" role="img" aria-label="Drei goldene Eier"></div>
  <article class="post abs" style="top:442px">
    <h1>Lindenhof Wissensportal</h1>
    <h2>Sie wollen die besten geschlossenen Fonds finden?</h2>
    <p><b>AIFM Richtlinie für geschlossene Fonds:</b><br>Auf Nimmerwiedersehen grauer Kapitalmarkt!<br>von Dr. Martin Albrecht am 15. Dezember 2010</p>
    <p><b>Der große Sieger ist der Anleger geschlossener Fonds</b><br>Die geschlossenen Fonds werden nun endgültig salonfähig und verabschieden sich vom Image des grauen Kapitalmarktes. Die jährliche Wertermittlungspflicht wird sich sehr positiv auf die Handelbarkeit der Produkte auswirken. Schon bei der Konstruktion der Fonds werden Emittenten zwangsläufig stärker auf das Thema der Fungibilität achten.<br>Der Gesamtmittelzufluß geschlossener Fonds dürfte bis 2020 sehr stark zunehmen und ein besonders starkes Wachstum erwarte ich für den Umsatz des Zweitmarktes für geschlossene Fonds.</p>
    <p>Der Markt für geschlossene Fonds wird nun erwachsen!</p>
  </article>
  <div class="meta abs" style="top:694px">08.05.2011 - Dr. Martin Albrecht - <svg width="9" height="8"><rect x=".5" y=".5" width="8" height="5" fill="none" stroke="#888"/></svg> 15 Kommentare - <svg width="7" height="9"><rect x=".5" y=".5" width="6" height="8" fill="none" stroke="var(--green)"/></svg> Kategorie: Fonds <span class="like">Empfehlen</span><span class="count">3</span></div>

  <article class="post abs" style="top:743px">
    <h1>Lindenhof Wissensportal</h1>
    <h2>Sie wollen die besten geschlossenen Fonds finden?</h2>
    <p><b>AIFM Richtlinie für geschlossene Fonds:</b><br>Auf Nimmerwiedersehen grauer Kapitalmarkt!<br>von Dr. Martin Albrecht am 15. Dezember 2010</p>
    <p><b>Der große Sieger ist der Anleger geschlossener Fonds</b><br>Die geschlossenen Fonds werden nun endgültig salonfähig und verabschieden sich vom Image des grauen Kapitalmarktes. Die jährliche Wertermittlungspflicht wird sich sehr positiv auf die Handelbarkeit der Produkte auswirken. Schon bei der Konstruktion der Fonds werden Emittenten zwangsläufig stärker auf das Thema der Fungibilität achten.<br>Der Gesamtmittelzufluß geschlossener Fonds dürfte bis 2020 sehr stark zunehmen und ein besonders starkes Wachstum erwarte ich für den Umsatz des Zweitmarktes für geschlossene Fonds.</p>
    <p>Der Markt für geschlossene Fonds wird nun erwachsen!</p>
  </article>
  <div class="meta abs" style="top:982px">08.05.2011 - Dr. Martin Albrecht - <svg width="9" height="8"><rect x=".5" y=".5" width="8" height="5" fill="none" stroke="#888"/></svg> 15 Kommentare - <svg width="7" height="9"><rect x=".5" y=".5" width="6" height="8" fill="none" stroke="var(--green)"/></svg> Kategorie: Fonds <span class="like">Empfehlen</span><span class="count">3</span></div>
</div>
</body>
</html>
```